Lawn sign for construction company

Would like this to be a very clean and high end design for luxury homes. We need a yard sign designed that includes the company logo, website, phone number and major service offerings (residential and commercial renovations and maintenance)
The company website is brackwellbuilders.com all other contact info is in the attachments
Target Market(s)
Luxury home owners and business owners
Industry/Entity Type
Construction/Home Improvement
Font styles to use
Other font styles liked:
- See company logo and other graphics included for title text fonts. All other fonts can be standard sans serif.
Colors
0054AA
0677BA
7BADD7
CADEEF
E8F1F8
Requirements
Must have
- Clean, easy to read design, would like 2 sided sign. A main sign side and back side which states “free estimates, and includes the website and phone number. Must also match the color scheme of the provided logo and other company images. Dark Navy blue primary color, gray secondary color, and orange as an accent color.
Nice to have
- 2nd sign side very simple design
Should not have
- Too many graphics limit to 1-3 colors

```html
<!DOCTYPE html>
<html lang="en">
<head>
<meta charset="utf-8">
<title>Kestrel Construction Co. – Lawn Sign</title>
<link rel="stylesheet" href="https://fonts.googleapis.com/css2?family=Rokkitt:wght@800&family=Open+Sans:wght@700&display=swap">
<style>
  :root {
    --navy: #101a35;
    --orange: #e57626;
    --white: #ffffff;
    --grey: #6b6b6b;
    --bg: #d2d3d5;
    --label: #3b3b3b;
  }
  * { box-sizing: border-box; margin: 0; padding: 0; }
  html, body { width: 1200px; height: 490px; overflow: hidden; }
  body { background: var(--bg); position: relative; font-family: "Rokkitt", serif; }

  .side-label {
    position: absolute; top: 38px; width: 476px; text-align: center;
    font-family: "Open Sans", sans-serif; font-weight: 700; font-size: 37px;
    color: var(--label);
  }
  .side-label--front { left: 103px; }
  .side-label--back  { left: 621px; }

  .sign {
    position: absolute; top: 121px; width: 476px; height: 312px;
    background: var(--orange); overflow: hidden;
  }
  .sign--front { left: 103px; }
  .sign--back  { left: 621px; }

  .sign__field { position: absolute; inset: 0; width: 100%; height: 100%; }

  .sign__text {
    position: absolute; left: 0; width: 100%; text-align: center;
    font-weight: 800; line-height: 1; white-space: nowrap;
  }

  .brand {
    position: absolute; left: 0; width: 100%;
    display: flex; flex-direction: column; align-items: center; gap: 8px;
  }
  .brand__mark { width: 44px; height: 44px; border-radius: 50%; background: var(--grey); }
  .brand__name {
    font-weight: 800; color: var(--orange); letter-spacing: 0.5px; line-height: 1;
  }
  .sign--front .brand { top: 54px; }
  .sign--front .brand__name { font-size: 30px; }
  .sign--back .brand { top: 66px; }
  .sign--back .brand__mark { width: 38px; height: 38px; }
  .sign--back .brand__name { font-size: 26px; }

  .rule {
    position: absolute; top: 197px; left: 75px; width: 325px; height: 2px;
    background: var(--orange);
  }
  .offer { top: 210px; font-size: 42px; color: var(--white); }
  .phone-front { top: 258px; font-size: 32px; color: var(--orange); }
  .phone-back { top: 194px; font-size: 36px; color: var(--white); }
  .website { top: 233px; font-size: 38px; color: var(--white); }
</style>
</head>
<body>
  <div class="side-label side-label--front">Front</div>
  <div class="side-label side-label--back">back</div>

  <section class="sign sign--front">
    <svg class="sign__field" viewBox="0 0 476 312" aria-hidden="true">
      <ellipse cx="238" cy="156" rx="228" ry="250" fill="var(--navy)"/>
    </svg>
    <div class="brand">
      <span class="brand__mark"></span>
      <span class="brand__name">KESTREL CONSTRUCTION CO.</span>
    </div>
    <div class="rule"></div>
    <p class="sign__text offer">FREE ESTIMATES</p>
    <p class="sign__text phone-front">+1 (555) 318-4072</p>
  </section>

  <section class="sign sign--back">
    <svg class="sign__field" viewBox="0 0 476 312" aria-hidden="true">
      <ellipse cx="238" cy="156" rx="228" ry="250" fill="var(--navy)"/>
    </svg>
    <div class="brand">
      <span class="brand__mark"></span>
      <span class="brand__name">KESTREL CONSTRUCTION CO.</span>
    </div>
    <p class="sign__text phone-back">+1 (555) 318-4072</p>
    <p class="sign__text website">brackwellbuilders.com</p>
  </section>
</body>
</html>
```